THE PRACTICE NAME "The Corvane MD" FOR A NEW MEDICAL PRACTICE STARTUP

THIS IS A BUSINESS CARD REQUEST FOR A KIDNEY DOCTOR's(NEPHROLOGIST) PRACTICE, THIS PRACTICE WILL BE IN EL PASO,TEXAS USA.OPEN TO INNOVATIVE IDEAS!

THE CORVANE MD ( NAME OF PRACTICE)

DEVESH R. MALHOTRA, MD FNKF FASN ( NAME OF PHYSICIAN WITH DEGREES)
BOARD CERTIFIED INTERNAL MEDICINE
BOARD CERTIFIED NEPHROLOGY
HYPERTENSION SPECIALIST

OFFICE ADDRESS, PHONE, FAX AND EMAIL PENDING

Steady Care. Healthier Days.(MOTTO) THE LOGO SHOILD REFLECT THIS MESSAGE. WE NEED A LOGO DESIGN WITH 2 KIDNEYS OR CAN BE ONE KIDNEY ALSO.

Target Market(s)

PATIENTS WITH KIDNEY DISEASE, HYPERTENSION, ENGLISH AND SPANISH SPEAKING POPULATION AND PATIENTS ON DIALYSIS

Industry/Entity Type

Health Care

Contact Information for Business Card

HYPERTENSION SPECIALIST

WEBSITE URL PENDING

Font styles to use
Serif
Sans Serif
Script

Colors
fbed38
ffc214
fbf289
fbee3e
5c5c5c
333333
1b1b1b
757575
d3d3d3

Requirements
Must have
• A KIDNEY LOGO
• NAME OF THE PRACTICE
Nice to have
• IF THE CARD CAN BE IN THE SHAPE OF A KIDNEY

```html
<!DOCTYPE html>
<html lang="en">
<head>
<meta charset="utf-8">
<title>The Corvane MD – Business Card</title>
<link rel="stylesheet" href="https://fonts.googleapis.com/css2?family=Open+Sans:ital,wght@0,400;0,600;1,700&display=swap">
<style>
  :root {
    --stage-center: #5b5b5b;
    --stage-edge: #3e3e3e;
    --card: #000000;
    --teal: #14a89d;
    --text-light: #d3d3d3;
    --text-soft: #c9c9c9;
  }
  html, body {
    margin: 0;
    padding: 0;
    width: 1200px;
    height: 999px;
    overflow: hidden;
  }
  body {
    position: relative;
    background: radial-gradient(ellipse at 50% 50%, var(--stage-center) 0%, #525252 55%, var(--stage-edge) 100%);
    font-family: "Open Sans", Arial, sans-serif;
  }
  .card-shape {
    position: absolute;
    left: 0;
    top: 0;
  }
  .brand {
    position: absolute;
    left: 405px;
    width: 400px;
    top: 158px;
    text-align: center;
  }
  .brand-dot {
    width: 92px;
    height: 92px;
    margin: 0 auto 58px;
    border-radius: 50%;
    background: var(--teal);
  }
  .brand-name {
    margin: 0;
    color: var(--teal);
    font-weight: 600;
    font-size: 34px;
    line-height: 1;
    white-space: nowrap;
  }
  .tagline {
    margin: 13px 0 0;
    color: var(--text-light);
    font-size: 20px;
    line-height: 1;
  }
  .physician {
    position: absolute;
    left: 342px;
    top: 436px;
  }
  .physician-name {
    margin: 0;
    padding-bottom: 6px;
    color: var(--teal);
    font-style: italic;
    font-weight: 700;
    font-size: 30px;
    line-height: 1.1;
    border-bottom: 3px solid var(--teal);
    display: inline-block;
    white-space: nowrap;
  }
  .credentials {
    list-style: none;
    margin: 15px 0 0;
    padding: 0;
    color: var(--text-light);
    font-size: 20.5px;
    line-height: 29px;
  }
  .address {
    position: absolute;
    left: 479px;
    top: 669px;
    margin: 0;
    color: var(--text-soft);
    font-style: normal;
    font-size: 21px;
    line-height: 28px;
  }
  .contacts {
    position: absolute;
    left: 479px;
    top: 753px;
    list-style: none;
    margin: 0;
    padding: 0;
    color: var(--text-soft);
    font-size: 21px;
  }
  .contacts li {
    display: flex;
    align-items: center;
    height: 33.5px;
  }
  .contact-icon {
    width: 22px;
    height: 22px;
    margin-right: 21px;
    flex: none;
  }
</style>
</head>
<body>

<svg class="card-shape" width="1200" height="999" viewBox="0 0 1200 999" aria-hidden="true">
  <path fill="var(--card)" d="M 600 98
    C 700 90, 835 130, 835 230
    C 835 320, 770 380, 703 440
    C 800 455, 895 520, 895 620
    C 895 720, 850 830, 838 880
    L 808 878
    C 822 800, 840 720, 828 660
    C 815 600, 775 578, 720 575
    C 790 630, 810 720, 775 800
    C 740 870, 660 912, 560 910
    C 430 908, 330 820, 312 700
    C 295 580, 320 450, 380 340
    C 440 230, 520 105, 600 98 Z"/>
</svg>

<header class="brand">
  <div class="brand-dot" aria-hidden="true"></div>
  <h1 class="brand-name">The Corvane MD</h1>
  <p class="tagline">Steady Care. Healthier Days</p>
</header>

<section class="physician">
  <h2 class="physician-name">DEVESH R. MALHOTRA</h2>
  <ul class="credentials">
    <li>MD FNKF FASN</li>
    <li>BOARD CERTIFIED INTERNAL MEDICINE</li>
    <li>BOARD CERTIFIED NEPHROLOGY</li>
    <li>HYPERTENSION SPECIALIST</li>
  </ul>
</section>

<address class="address">suit # 00, Lorem ipsum<br>Lorem Lorem ipsum</address>

<ul class="contacts">
  <li>
    <svg class="contact-icon" viewBox="0 0 22 22" aria-label="Phone">
      <rect width="22" height="22" rx="4" fill="var(--teal)"/>
      <path d="M7 4 L9.5 4 L10.5 8 L8.8 9.3 C9.6 11.2 10.8 12.4 12.7 13.2 L14 11.5 L18 12.5 L18 15 C18 16.5 16.5 17.5 15 17.2 C9.8 16.2 5.8 12.2 4.8 7 C4.5 5.5 5.5 4 7 4 Z" fill="var(--card)"/>
    </svg>
    <span>000-000-0000</span>
  </li>
  <li>
    <svg class="contact-icon" viewBox="0 0 22 22" aria-label="Fax">
      <rect x="5" y="1" width="12" height="7" fill="var(--teal)"/>
      <rect x="1" y="9" width="20" height="8" rx="1.5" fill="var(--teal)"/>
      <rect x="5" y="14" width="12" height="7" fill="var(--teal)"/>
      <rect x="7" y="16" width="8" height="1.5" fill="var(--card)"/>
    </svg>
    <span>000-000-0000</span>
  </li>
  <li>
    <svg class="contact-icon" viewBox="0 0 22 22" aria-label="Email">
      <path d="M11 1 L21 8 L21 21 L1 21 L1 8 Z" fill="var(--teal)"/>
      <path d="M3 9 L11 15 L19 9" stroke="var(--card)" stroke-width="1.8" fill="none"/>
    </svg>
    <span>hello@corvanemd.com</span>
  </li>
</ul>

</body>
</html>
```